Flyer-Design für Beratungsunternehmen
Vielen Dank für die professionelle und überdurchschnittliche Unterstützung
Zielgruppe
Supervision, Coaching, Beratung
Plus digitale Beratung via App, sonstiger moderner Medien
für Organisationen, Firmen, Institutionen, Privatpersonen
Aufgabenstellung
Kreatives Design, modern, hochwertig
symphatisch, vertrauensvoll, transparent, ansprechend
Texte, Inhalte und Bilder siehe download
Sehr wichtig corporate design laut homepage www.wegweiserlotsenhaus.de

```html
<!DOCTYPE html>
<html lang="de">
<head>
<meta charset="utf-8">
<title>Wegweiser Lotsenhaus – Flyer</title>
<link rel="stylesheet" href="https://fonts.googleapis.com/css2?family=Oswald:wght@500;600&family=Questrial&display=swap">
<style>
  :root {
    --orange: #ee7d1b;
    --green: #8dbf2b;
    --green-soft: #cfe2a7;
    --text: #4b4b4b;
    --paper: #f4f4f4;
    --white: #ffffff;
    --ring: #e2e2e2;
  }
  * { margin: 0; padding: 0; box-sizing: border-box; }
  html, body { width: 1200px; height: 600px; overflow: hidden; }
  body {
    position: relative;
    background: var(--paper);
    font-family: "Questrial", "Century Gothic", sans-serif;
    color: var(--text);
    font-size: 10.4px;
    line-height: 14.1px;
  }
  .backdrop { position: absolute; inset: 0; }

  .brand-badge {
    position: absolute; left: -22px; top: -52px;
    width: 226px; height: 226px; border-radius: 50%;
    background: var(--white);
    box-shadow: 0 0 0 5px var(--ring);
    display: flex; align-items: center; justify-content: center;
    padding-top: 48px; padding-left: 18px;
  }
  .brand-name {
    font-size: 17px; line-height: 19px; color: #1f1f1f;
    text-transform: uppercase; letter-spacing: 0.5px; text-align: center;
  }

  .photo {
    position: absolute; border-radius: 50%;
    box-shadow: 0 0 0 5px var(--ring);
  }
  .photo-portrait {
    left: 1021px; top: -30px; width: 186px; height: 186px;
    background: linear-gradient(160deg, #c9d3d6 0%, #8e9a93 45%, #3b4a5c 75%, #b98e6a 100%);
  }
  .photo-lake {
    left: 401px; top: 482px; width: 224px; height: 224px;
    background: linear-gradient(180deg, #5d6a4e 0%, #c9b79a 40%, #e8d6b8 55%, #8a7d6d 100%);
  }

  .block { position: absolute; }
  .title-main {
    font-family: "Oswald", "Arial Narrow", sans-serif; font-weight: 600;
    color: var(--orange); font-size: 17.5px; line-height: 22px;
    text-transform: uppercase; letter-spacing: 0.3px;
  }
  .title-sub {
    color: var(--green); font-size: 14.5px; line-height: 16px;
    text-transform: uppercase; letter-spacing: 0.1px;
  }
  .label { font-size: 12.5px; line-height: 14px; color: var(--text); }

  .list { list-style: none; }
  .list li { position: relative; padding-left: 17px; line-height: 12.2px; }
  .list.tick li::before {
    content: "✔"; position: absolute; left: 0; top: 0;
    color: var(--orange); font-size: 11px;
  }
  .list.plus li::before, .list.plus li::after {
    content: ""; position: absolute; background: var(--green);
  }
  .list.plus li::before { left: 1px; top: 5px; width: 8px; height: 2px; }
  .list.plus li::after { left: 4px; top: 2px; width: 2px; height: 8px; }

  .formats {
    display: grid; grid-template-columns: 108px 100px; row-gap: 3px;
    list-style: none; margin-left: 17px;
  }
  .formats li { position: relative; padding-left: 11px; line-height: 12px; }
  .formats li::before {
    content: ""; position: absolute; left: 0; top: 4px;
    width: 4px; height: 4px; background: var(--text);
  }

  .conclusion { text-transform: uppercase; font-size: 10.6px; color: #333; }
</style>
</head>
<body>

<svg class="backdrop" width="1200" height="600" viewBox="0 0 1200 600" aria-hidden="true">
  <path d="M0 0 H1200 V40 L1030 46 Q600 138 150 88 L0 90 Z" fill="#ffffff"/>
  <path d="M160 90 Q600 128 1025 46 L1030 50 Q600 144 160 90 Z" fill="#cfe2a7"/>
</svg>

<div class="brand-badge">
  <p class="brand-name">Wegweiser<br>Lotsenhaus</p>
</div>

<div class="photo photo-portrait" role="img" aria-label="Foto: Beraterin lächelnd am Laptop in einem hellen Büro"></div>
<div class="photo photo-lake" role="img" aria-label="Foto: Frau meditiert auf einem Holzsteg am nebligen See im Gegenlicht"></div>

<!-- Spalte 1 -->
<section class="block" style="left:46px; top:157px; width:240px;">
  <h1 class="title-main">Meine Fachgebiete für ein<br>besseres Wohlfühlen</h1>
</section>
<section class="block" style="left:46px; top:221px; width:240px;">
  <h2 class="title-sub">Systemische Supervision</h2>
  <p style="margin-top:6px;">Bietet Ihnen und Ihrem Team einen geschützten Raum Ihren Arbeitskontext, komplexe Anforderun-gen und Strukturen moderiert zu reflektieren sowie Konflikte, Rollen und Fragestellungen zu klären.</p>
</section>
<section class="block" style="left:46px; top:321px; width:240px;">
  <h3 class="label">Ziele</h3>
  <ul class="list tick" style="margin-top:3px;">
    <li style="margin-bottom:8px;">Rollensicherheit und Teamfähigkeit weiterentwickeln</li>
    <li style="margin-bottom:9px;">tiefes Verständnis der beruflichen Situation, Handlungsmöglichkeiten und Perspektiven entwickeln.</li>
    <li style="margin-bottom:9px;">Qualitätssicherung.</li>
    <li style="margin-bottom:8px;">Stärken &amp; Kompetenzen bewusst machen</li>
    <li style="margin-bottom:8px;">langfristig die Freude an Ihrer Arbeit erhalten</li>
  </ul>
  <ul class="formats">
    <li>Einzelsupervision</li><li>Gruppensupervision</li>
    <li>Teamsupervision</li><li>Fallsupervision</li>
  </ul>
</section>

<!-- Spalte 2 -->
<section class="block" style="left:310px; top:159px; width:240px;">
  <h2 class="title-sub">Systemisches Coaching</h2>
  <p style="margin-top:7px;">Erweitern Sie Ihre beruflichen Handlungsstrategien und machen Sie Ihre Stärken und Fähigkeiten nutz-bar, um Ihr Ziel zu erreichen. Persönliche Zufriedenheit und professionelle Leistungsfähigkeit stehen im Fokus.</p>
</section>
<section class="block" style="left:310px; top:270px; width:240px;">
  <h2 class="title-sub">Lifecoaching</h2>
  <p style="margin-top:7px;">Im Mittelpunkt stehen Ihre persönlichen Sorgen, Wünsche und Anliegen.<br>Gemeinsam erarbeiten wir Ihr konkretes Ziel und gehen auf Schatzsuche, entdecken neue Perspe-ktiven, Handlungsoptionen, die Sie Schritt für Schritt Ihrem persönlichen Erfolg näherbringen.</p>
</section>
<section class="block" style="left:310px; top:398px; width:240px;">
  <h2 class="title-sub">Digitale Beratung</h2>
  <p style="margin-top:7px;">Endlich können Sie ganz einfach ungenutzte Zeit auf dem Weg zur Arbeit, in Wartebereichen oder Zwischendurch nutzen, um Ihre<br>Ziele und Wünsche wahr<br>werden zu lassen.</p>
</section>

<!-- Spalte 3 -->
<section class="block" style="left:641px; top:157px; width:240px;">
  <h2 class="title-main">Bei mir erhalten Sie</h2>
  <ul class="list plus" style="margin-top:10px;">
    <li style="margin-bottom:8px;">Eigenen geschützten Account / eigene App</li>
    <li style="margin-bottom:9px;">24 Stunden / 7 Tage in der Woche Zugang</li>
    <li style="margin-bottom:9px;">Visualisierung Ihrer Erfolge</li>
    <li style="margin-bottom:8px;">Eine Vielzahl an Tools und Fragebögen zur konkreten Umsetzungsbegleitung</li>
    <li style="margin-bottom:9px;">Responsive Design / nutzbar auf dem Smart-phone, Tablet, PC</li>
    <li style="margin-bottom:9px;">Höchstmaß an Flexibilität</li>
    <li>Extrem effizient und dadurch zeit- und geldspa-rend</li>
  </ul>
  <p style="margin-top:6px;">Entscheiden Sie selbst, ob Sie die Möglichkeit der digitalen Beratung zusätzlich nutzen wollen oder diese die Sitzungen vor Ort komplett ersetzen soll. Sie möchten auf die klassischen Sitzungen nicht verzichten?</p>
  <p style="margin-top:14px;">Nutzen Sie die digitale Begleitung dazwischen und/oder nach dem gesamten Beratungsprozess (Follow-Up). So sichern Sie Ihre Erfolge auch lang-fristig und brauchen vor Herausforderungen und Widerständen im Alltag keine Angst mehr haben.</p>
</section>

<!-- Spalte 4 -->
<section class="block" style="left:909px; top:159px; width:270px;">
  <h2 class="title-sub">Vorzüge</h2>
  <div style="display:flex; margin-top:7px;">
    <ul class="list tick" style="width:124px;">
      <li style="margin-bottom:7px;">Effizienz,</li>
      <li style="margin-bottom:7px;">Mobilität,</li>
      <li>Flexibilität,</li>
    </ul>
    <ul class="list tick">
      <li style="margin-bottom:7px;">Nachhaltigkeit,</li>
      <li style="margin-bottom:7px;">Sicherheit,</li>
      <li>großmögliche Anonymität.</li>
    </ul>
  </div>
  <p class="conclusion" style="margin-top:19px;">➜ Fazit: Sparen Sie Zeit und Geld!</p>
</section>
<section class="block" style="left:909px; top:288px; width:280px;">
  <h2 class="title-sub">Mein Format für Ihren Mehrwert!</h2>
  <ul class="list tick" style="margin-top:8px;">
    <li style="margin-bottom:7px;">Nachhaltiger Erfolg durch digitale Begleitung</li>
    <li style="margin-bottom:7px;">Der rote Faden des Veränderungsprozesses sichtbar</li>
    <li style="margin-bottom:8px;">Beste Transfer- &amp; Nachbegleitung</li>
    <li>Zeit- &amp; Ortsunabhängiges Coaching</li>
  </ul>
</section>
<section class="block" style="left:909px; top:407px; width:280px;">
  <h2 class="title-sub">Meine Werte und Haltung</h2>
  <ul class="list tick" style="margin-top:8px;">
    <li style="margin-bottom:6.5px;">Wertschätzung, Ressourcenorientierung und Respekt</li>
    <li style="margin-bottom:6.5px;">Systemisch</li>
    <li style="margin-bottom:6.5px;">Lösungsorientiert</li>
    <li style="margin-bottom:6.5px;">Kompetenz und Methodenvielfalt</li>
    <li style="margin-bottom:6.5px;">Nicht für, sondern mit Ihnen!</li>
    <li style="margin-bottom:7.5px;">Transparenz und Struktur</li>
    <li>Verschwiegenheit und Vertrauen</li>
  </ul>
</section>

</body>
</html>
```